Borvik Garage Post Card

We are a concrete coating installation company. We install Epoxy coatings, Life Time Adhesion Warranty Primer, Deck Coatings, Decorative Concrete Coatings, Concrete Staining, Garage Cabinets and storage solutions. Borvik Garage & Concrete focuses on providing our customers with a professional installation using commercial and industrial grade products. During the installation process, we use new generation products that are more environmentally friendly than prior generation epoxies. All of our products are Made In The USA. Ask about our Lifetime Warranty!
Updates

Target Market(s)

upper middle class

Industry/Entity Type

Industrial

Requirements
Must have
• Would like to have a have images on the card so people see a couple samples.
contact information:
borvikgarageandconcrete.example
555-318-4726
Serving Middle Tennessee
Nice to have
• contact information

```html
<!DOCTYPE html>
<html lang="en">
<head>
<meta charset="utf-8">
<title>Borvik Garage &amp; Concrete – Post Card</title>
<link rel="stylesheet" href="https://fonts.googleapis.com/css2?family=Lato:wght@700&family=PT+Sans:wght@400;700&display=swap">
<style>
  :root {
    --card-bg: #e8e9eb;
    --brand-blue: #1a74c2;
    --ink: #2f2f31;
    --ink-dark: #111;
    --stone-dark: #c4661c;
    --stone-mid: #e08a35;
    --stone-light: #d9a865;
    --stone-pale: #c9ab7f;
    --badge-navy: #1e2a5e;
    --badge-red: #c0262d;
    --badge-silver: #b9bcc2;
  }
  * { margin: 0; padding: 0; box-sizing: border-box; }
  html, body { width: 1200px; height: 946px; overflow: hidden; background: var(--card-bg); }
  .postcard {
    position: relative;
    width: 1200px;
    height: 946px;
    overflow: hidden;
    background: var(--card-bg);
    font-family: "PT Sans", sans-serif;
    color: var(--ink);
  }
  .sample-photo { position: absolute; inset: 0; }
  .brand-name {
    position: absolute;
    left: 215px;
    top: 200px;
    display: flex;
    align-items: center;
    gap: 12px;
    font-weight: 700;
    font-size: 52px;
    color: var(--ink-dark);
    letter-spacing: 1px;
  }
  .brand-mark { width: 22px; height: 22px; background: var(--ink-dark); border-radius: 50%; }
  .headline {
    position: absolute;
    right: 53px;
    top: 38px;
    text-align: right;
    font-family: "Lato", sans-serif;
    font-weight: 700;
    font-size: 57px;
    line-height: 66px;
    color: var(--brand-blue);
    letter-spacing: 0.5px;
  }
  .offer-title {
    position: absolute;
    right: 53px;
    top: 203px;
    font-weight: 700;
    font-size: 52px;
    line-height: 62px;
    color: var(--brand-blue);
  }
  .service-list {
    position: absolute;
    right: 53px;
    top: 278px;
    list-style: none;
    text-align: right;
  }
  .service-list li {
    display: flex;
    justify-content: flex-end;
    align-items: center;
    gap: 10px;
    font-size: 27px;
    line-height: 36.5px;
    color: var(--ink);
  }
  .tick { width: 24px; height: 24px; flex: none; }
  .contact-web {
    position: absolute;
    left: 38px;
    top: 862px;
    font-size: 23px;
    font-weight: 700;
    line-height: 34px;
    color: var(--ink);
  }
  .contact-web .site { display: flex; align-items: center; gap: 10px; }
  .globe { width: 22px; height: 22px; }
  .contact-phone {
    position: absolute;
    left: 507px;
    top: 862px;
    display: flex;
    align-items: center;
    gap: 12px;
    font-size: 48px;
    color: var(--ink-dark);
  }
  .phone-icon { width: 58px; height: 58px; }
  .badges { position: absolute; left: 0; top: 0; }
</style>
</head>
<body>
<main class="postcard">

  <svg class="sample-photo" width="1200" height="946" viewBox="0 0 1200 946" role="img" aria-label="Close-up photo of textured decorative stamped concrete in orange and tan tones">
    <defs>
      <linearGradient id="stoneTone" x1="0" y1="0" x2="1" y2="1">
        <stop offset="0" stop-color="var(--stone-pale)"/>
        <stop offset="0.3" stop-color="var(--stone-dark)"/>
        <stop offset="0.6" stop-color="var(--stone-mid)"/>
        <stop offset="1" stop-color="var(--stone-light)"/>
      </linearGradient>
    </defs>
    <path d="M0 7 C 60 130, 130 230, 214 297 C 300 370, 390 420, 471 446 C 600 500, 720 540, 814 551 C 950 575, 1080 590, 1200 591 L 1200 639 C 1000 720, 780 800, 514 832 C 330 845, 150 800, 0 749 Z" fill="url(#stoneTone)"/>
  </svg>

  <div class="brand-name"><span class="brand-mark"></span>BORVIK</div>

  <h1 class="headline">A CONCRETE COATING<br>INSTALLATION COMPANY</h1>

  <h2 class="offer-title">We Offer</h2>

  <ul class="service-list">
    <li><svg class="tick" viewBox="0 0 24 24"><circle cx="11" cy="13" r="9.5" fill="none" stroke="var(--ink)" stroke-width="1.8"/><path d="M6 13 l4 5 L21 3" fill="none" stroke="var(--brand-blue)" stroke-width="3"/></svg>Epoxy Coatings</li>
    <li><svg class="tick" viewBox="0 0 24 24"><circle cx="11" cy="13" r="9.5" fill="none" stroke="var(--ink)" stroke-width="1.8"/><path d="M6 13 l4 5 L21 3" fill="none" stroke="var(--brand-blue)" stroke-width="3"/></svg>Life Time Adhesion Warranty Primer</li>
    <li><svg class="tick" viewBox="0 0 24 24"><circle cx="11" cy="13" r="9.5" fill="none" stroke="var(--ink)" stroke-width="1.8"/><path d="M6 13 l4 5 L21 3" fill="none" stroke="var(--brand-blue)" stroke-width="3"/></svg>Deck Coatings</li>
    <li><svg class="tick" viewBox="0 0 24 24"><circle cx="11" cy="13" r="9.5" fill="none" stroke="var(--ink)" stroke-width="1.8"/><path d="M6 13 l4 5 L21 3" fill="none" stroke="var(--brand-blue)" stroke-width="3"/></svg>Decorative Concrete Coatings</li>
    <li><svg class="tick" viewBox="0 0 24 24"><circle cx="11" cy="13" r="9.5" fill="none" stroke="var(--ink)" stroke-width="1.8"/><path d="M6 13 l4 5 L21 3" fill="none" stroke="var(--brand-blue)" stroke-width="3"/></svg>Concrete Staining</li>
    <li><svg class="tick" viewBox="0 0 24 24"><circle cx="11" cy="13" r="9.5" fill="none" stroke="var(--ink)" stroke-width="1.8"/><path d="M6 13 l4 5 L21 3" fill="none" stroke="var(--brand-blue)" stroke-width="3"/></svg>Garage Cabinets</li>
    <li><svg class="tick" viewBox="0 0 24 24"><circle cx="11" cy="13" r="9.5" fill="none" stroke="var(--ink)" stroke-width="1.8"/><path d="M6 13 l4 5 L21 3" fill="none" stroke="var(--brand-blue)" stroke-width="3"/></svg>Storage Solutions</li>
  </ul>

  <svg class="badges" width="1200" height="946" viewBox="0 0 1200 946" aria-hidden="true">
    <rect x="983" y="750" width="88" height="75" fill="var(--badge-red)" stroke="var(--ink-dark)" stroke-width="3"/>
    <rect x="1080" y="758" width="86" height="61" rx="12" fill="var(--badge-navy)"/>
    <path d="M968 852 Q1000 838 1031 852 L1031 880 Q1026 905 1000 914 Q974 905 968 880 Z" fill="var(--badge-silver)"/>
    <path d="M974 857 Q1000 846 1025 857 L1025 880 Q1021 899 1000 907 Q979 899 974 880 Z" fill="var(--badge-red)"/>
    <rect x="1035" y="852" width="139" height="34" rx="4" fill="var(--badge-navy)"/>
    <rect x="1035" y="888" width="139" height="18" rx="3" fill="var(--badge-red)"/>
  </svg>

  <div class="contact-web">
    <div class="site">
      <svg class="globe" viewBox="0 0 22 22"><g fill="none" stroke="var(--ink)" stroke-width="1.6"><circle cx="11" cy="11" r="9.5"/><ellipse cx="11" cy="11" rx="4.5" ry="9.5"/><path d="M1.5 11h19M3 6h16M3 16h16"/></g></svg>
      borvikgarageandconcrete.example
    </div>
    <div class="area">Serving Middle Tennessee</div>
  </div>

  <div class="contact-phone">
    <svg class="phone-icon" viewBox="0 0 58 58"><circle cx="29" cy="29" r="26" fill="none" stroke="var(--ink-dark)" stroke-width="3"/><path d="M24 14 q-8 4 -6 16 q3 12 12 15 l4 -6 -6 -4 -3 2 q-4 -5 -4 -12 l3 -2 -1 -8 z" fill="var(--ink-dark)"/></svg>
    555-318-4726
  </div>

</main>
</body>
</html>
```